Delan Morvish Golf Instruction

I need a web design for a golf instruction website. My goal is to gain more exposure through this site. I want this site to be a source for golf knowledge and instruction by providing instructional videos and instructional literature. I want the site to have colors navy blue(tulsa ravenhawks blue) and silver. I am also open to other color schemes. The main website to imitate is trevolkingsby.example. I want tabs/links at the top of the site that read: Home, About, Video Instruction, Instruction, and Golf Blog. Other sites to reference are Rolf Pettiber Golf and steadyarcgolfmotion.example. A main feature that must be included is online video lessons like on rolfpettiber.example. I have software that provides me the ability to take a video of a golf swing and record a voice video lesson. Reference the example video on rolfpettiber.example.

The main goal for this web design is to have an "outline" in place so that I can go back and input the videos and literature.

Reason: I need more time to wait for changes. I like all the designs.

Target Market(s)

My target market is golfer of all ages and abilities: juniors, adults, men, and women.

Industry/Entity Type

Software

Requirements
Must have
• Capability to input videos and literature onto the site.
"Lead Instructor at Larkmoor Golf Club" title.
A very visible "Larkmoor Golf Club" logo.
Friendspace, Chirpline, and ClipTube quicklinks.

```html
<!DOCTYPE html>
<html lang="en">
<head>
<meta charset="utf-8">
<title>Larkmoor Golf Club – Lead Instructor at Larkmoor Golf Club</title>
<link href="https://fonts.googleapis.com/css2?family=Ubuntu:ital,wght@0,400;0,500;0,700;1,400;1,500&family=Arimo:wght@400;700&display=swap" rel="stylesheet">
<style>
:root{
  --navy:#1f2f6e;
  --royal:#3f56a8;
  --text:#333;
  --page:#f3f3f3;
  --link:#1f44a8;
  --footer:#3b3b3b;
  --footer-text:#bdbdbd;
  --orange:#e2761b;
  --friendspace:#3a5ca8;
  --chirpline:#49b3d6;
  --cliptube:#c8302a;
  --turf:#3f9a2e;
}
*{box-sizing:border-box;margin:0;padding:0}
html,body{width:966px;height:1200px;overflow:hidden}
body{position:relative;background:var(--page);font-family:Arimo,Arial,sans-serif;color:var(--text)}
.abs{position:absolute}
.topbar{left:0;top:0;width:966px;height:40px;background:linear-gradient(#fdfdfd,#e9e9e9)}
.hero{left:0;top:40px;width:966px;height:357px;background:linear-gradient(180deg,#3b54a6 0%,#3550a2 45%,#1e2d6c 100%)}
.follow{left:687px;top:8px;font:500 14px Ubuntu,sans-serif;color:#444;display:flex;align-items:center;gap:8px}
.follow a{display:block;width:22px;height:22px;border-radius:50%}
.logo-card{left:107px;top:16px;width:221px;height:129px;background:#fff;box-shadow:0 2px 4px rgba(0,0,0,.25);display:flex;flex-direction:column;justify-content:center;padding-left:16px}
.logo-card .name{font:700 34px Ubuntu,sans-serif;color:var(--navy);letter-spacing:1px;line-height:1}
.logo-card .sub{font:700 22px Ubuntu,sans-serif;color:var(--navy);line-height:1.2}
.nav{left:415px;top:30px;height:46px;width:480px}
.nav a{font:400 12px Ubuntu,sans-serif;color:#fff;text-decoration:none;position:absolute;top:22px;white-space:nowrap}
.nav .home{left:0;top:0;width:68px;height:46px;background:linear-gradient(#fff,#e1e1e1);color:#333;display:flex;align-items:center;justify-content:center;padding-top:7px}
.nav .sep{position:absolute;top:18px;height:24px;border-left:1px dotted #7d8ed0}
.video{left:88px;top:175px;width:504px;height:295px;background:#d8d8d8;border:1px solid #bbb;padding:5px}
.video .screen{width:493px;height:267px;background:linear-gradient(180deg,#5aa844,#3a8f2a)}
.video .controls{width:493px;height:19px;background:linear-gradient(#3a3a3a,#151515);display:flex;align-items:center;gap:6px;padding:0 6px;font:9px Arimo,sans-serif;color:#ddd}
.video .track{flex:1;height:2px;background:#666;position:relative}
.video .track i{position:absolute;left:0;top:0;width:68px;height:2px;background:#ccc}
.play{left:310px;top:292px}
.hero-title{left:609px;top:170px;font:400 29px Ubuntu,sans-serif;color:#fff;white-space:nowrap}
.hero-title b{font-weight:700}
.hero-copy{left:610px;top:214px;width:264px;font-size:9.7px;line-height:16.1px;color:#fff;text-align:justify}
.lessons-tab{left:624px;top:356px;width:236px;height:56px;background:linear-gradient(#fff,#ececec);display:flex;align-items:center;justify-content:center;font:400 25px Ubuntu,sans-serif;color:var(--navy);padding-top:6px}
.lessons-base{left:614px;top:396px;width:260px;height:16px;background:#dedede;border-radius:8px;z-index:-1}
.partner{left:696px;top:450px;display:flex;align-items:center;gap:6px}
.partner .mark{width:16px;height:16px;border-radius:50%;background:var(--orange)}
.partner span{font:700 26px Ubuntu,sans-serif;color:var(--navy)}
.section-title{left:144px;top:502px;font:400 19.5px Ubuntu,sans-serif;color:var(--navy)}
.flag{left:95px;top:494px}
.blog-panel{left:88px;top:541px;width:550px;height:511px;background:#fff;border:1px solid #ddd;box-shadow:0 1px 3px rgba(0,0,0,.12)}
.post-title{font:400 14.5px Ubuntu,sans-serif;color:var(--navy);white-space:nowrap}
.post-meta{font:italic 8px Ubuntu,sans-serif;color:#333}
.post-body{width:408px;font-size:9.6px;line-height:14.5px;color:#333;letter-spacing:.15px}
.thumb{width:84px;height:82px;border:1px solid #ddd;padding:2px;background:#fff}
.thumb div{width:100%;height:100%;background:var(--turf)}
.like{width:47px;height:18px;border:1px solid #aab;background:linear-gradient(#fff,#e9e9e9);font:700 9px Arimo,sans-serif;color:#2a3a6a;display:flex;align-items:center;justify-content:center;gap:4px}
.like i{width:10px;height:9px;border:1px solid #2a4a8a;border-radius:1px}
.more{width:57px;height:16px;background:#e8e8e8;font:italic 8px Ubuntu,sans-serif;color:#333;display:flex;align-items:center;justify-content:center}
.rule{left:96px;width:526px;border-top:1px dotted #999}
.pager{top:1067px;height:16px;font:italic 500 8.5px Ubuntu,sans-serif;display:flex;align-items:center;justify-content:center}
.pager.dark{background:var(--navy);color:#fff;width:52px}
.pager.num{background:#d8d8d8;color:#333;width:18px}
.newsletter{left:664px;top:532px;width:217px;height:178px;background:#fff;border:1px solid #e0e0e0;border-radius:8px;box-shadow:0 3px 4px rgba(0,0,0,.08)}
.newsletter h3{position:absolute;left:49px;top:14px;font:700 13.5px Ubuntu,sans-serif;color:#444;white-space:nowrap}
.newsletter h3 span{color:var(--link)}
.newsletter p{position:absolute;left:11px;top:44px;width:196px;font:400 9px/13px Ubuntu,sans-serif;color:#444;text-align:justify}
.newsletter label{position:absolute;font:400 10px Ubuntu,sans-serif;color:#444}
.field{position:absolute;left:61px;width:139px;height:19px;border:2px solid #eee;border-radius:10px;background:#fff}
.subscribe{position:absolute;left:120px;top:139px;width:80px;height:27px;border-radius:14px;background:linear-gradient(#3b6fe0,#1238a8);border:2px solid #c8d4f3;box-shadow:0 0 0 1px #1a3aa0;color:#fff;font:400 10px Arimo,sans-serif;display:flex;align-items:center;justify-content:center}
.tabs{left:662px;top:733px;width:219px;height:248px}
.tabs .head{display:flex;height:23px;font:500 9.5px Ubuntu,sans-serif;color:#555}
.tabs .head div{width:72px;display:flex;align-items:center;justify-content:center}
.tabs .head .on{background:#fff;border:1px solid #ddd;border-bottom:none;color:var(--link)}
.tabs .body{background:#fff;border:1px solid #ddd;height:225px;padding:0 10px}
.item{border-bottom:1px solid #e2e2e2;padding:10px 0 6px}
.item:last-child{border-bottom:none}
.item p{font:400 9px/11px Ubuntu,sans-serif;color:#333;text-align:justify;text-align-last:left}
.item .row{display:flex;justify-content:space-between;font:700 italic 8.8px Ubuntu,sans-serif;color:var(--link);margin-top:3px;padding:0 1px}
.social{left:688px;display:flex;align-items:center;gap:8px}
.social .sq{width:26px;height:26px;border-radius:4px}
.social .t1{font:400 10.5px Ubuntu,sans-serif;color:var(--link);line-height:1}
.social .t2{font:500 17px Ubuntu,sans-serif;color:var(--link);line-height:1}
.footer{left:0;top:1108px;width:966px;height:92px;background:var(--footer)}
.footer .brand{position:absolute;left:98px;top:22px;font:700 24px Ubuntu,sans-serif;color:#bcbcbc;line-height:1}
.footer .brand small{display:block;font:700 15px Ubuntu,sans-serif}
.footer nav{position:absolute;left:325px;top:30px;font:400 9.8px Arimo,sans-serif;color:var(--footer-text);white-space:nowrap;word-spacing:2px}
.footer .copy{position:absolute;left:313px;top:47px;font:400 9.8px Arimo,sans-serif;color:var(--footer-text);white-space:nowrap}
.footer address{position:absolute;right:95px;top:14px;font:normal 9.8px/16px Arimo,sans-serif;color:var(--footer-text);text-align:right}
.footer address b{font-weight:700}
</style>
</head>
<body>
<div class="abs topbar"></div>
<div class="abs hero"></div>

<div class="abs follow">Follow us on
  <a href="#" aria-label="Friendspace" title="Friendspace" style="background:var(--friendspace)"></a>
  <a href="#" aria-label="Chirpline" title="Chirpline" style="background:var(--chirpline)"></a>
  <a href="#" aria-label="ClipTube" title="ClipTube" style="background:var(--cliptube)"></a>
</div>

<div class="abs logo-card" aria-label="Larkmoor Golf Club – Lead Instructor at Larkmoor Golf Club">
  <div class="name">LARKMOOR</div>
  <div class="sub">Golf Club</div>
</div>

<nav class="abs nav">
  <a class="home" href="#">Home</a>
  <span class="sep" style="left:92px"></span>
  <a href="#" style="left:110px">About</a>
  <span class="sep" style="left:162px"></span>
  <a href="#" style="left:185px">Video Instruction</a>
  <span class="sep" style="left:300px"></span>
  <a href="#" style="left:321px">Instruction</a>
  <span class="sep" style="left:403px"></span>
  <a href="#" style="left:423px">Golf Blog</a>
</nav>

<div class="abs video">
  <div class="screen" role="img" aria-label="Video lesson: golfer swinging on a fairway"></div>
  <div class="controls">
    <svg width="8" height="8"><rect width="7" height="7" fill="#ddd"/></svg>
    <svg width="14" height="14"><rect width="14" height="14" fill="#555"/><rect x="4" y="3" width="2" height="8" fill="#fff"/><rect x="8" y="3" width="2" height="8" fill="#fff"/></svg>
    <div class="track"><i></i></div>
    <span>00:38/01:29</span>
    <svg width="40" height="8"><rect x="0" y="1" width="7" height="6" fill="#ccc"/><rect x="16" y="1" width="7" height="6" fill="#ccc"/><rect x="32" y="1" width="7" height="6" fill="#ccc"/></svg>
  </div>
</div>
<svg class="abs play" width="60" height="60" viewBox="0 0 60 60">
  <circle cx="30" cy="30" r="28" fill="rgba(40,40,40,.75)" stroke="#ddd" stroke-width="3"/>
  <path d="M23 17 L43 30 L23 43 Z" fill="#fff"/>
</svg>

<h1 class="abs hero-title">Larkmoor <b>Golf Club</b></h1>
<p class="abs hero-copy">Lorem Ipsum is simply dummy text of the printing and type-setting industry. Lorem Ipsum has been the industry's standard dummy text ever since the 1500s, when an unknown printer took a galley of type and scrambled it to make a type specimen book. It has survived not only five centuries, but also the leap into electronic typesetting, remaining essentially unchanged.</p>

<div class="abs lessons-base"></div>
<div class="abs lessons-tab">Online Lessons</div>

<div class="abs partner"><span class="mark"></span><span>Kestrel Golf</span></div>

<svg class="abs flag" width="44" height="44" viewBox="0 0 44 44">
  <line x1="4" y1="42" x2="14" y2="4" stroke="#999" stroke-width="2"/>
  <path d="M14 4 L42 10 L34 30 L9 22 Z" fill="#d9441c"/>
  <circle cx="25" cy="16" r="6" fill="#fff"/>
</svg>
<h2 class="abs section-title">Recent Blogs</h2>

<div class="abs blog-panel"></div>

<article>
  <h3 class="abs post-title" style="left:96px;top:556px">Topping the Ball</h3>
  <div class="abs like" style="left:575px;top:562px"><i></i>Like</div>
  <p class="abs post-meta" style="left:95px;top:581px">Submitted by Larkmoor Golf Club on June 30th, 2011</p>
  <div class="abs thumb" style="left:105px;top:607px"><div role="img" aria-label="Photo: golfers on personal transporters"></div></div>
  <p class="abs post-body" style="left:209px;top:604px">Lorem Ipsum is simply dummy text of the printing and typesetting industry. Lorem Ipsum has been the industry's standard dummy text ever since the 1500s, when an unknown printer took a galley of type and scrambled it to make a type specimen book. It has survived not only five centuries, but also the leap into electronic typesetting, remaining essentially unchanged. It was popularised in the 1960s with the release of Typorama sheets containing Lorem Ipsum passages...</p>
  <div class="abs more" style="left:564px;top:697px">Read more...</div>
</article>
<div class="abs rule" style="top:723px"></div>

<article>
  <h3 class="abs post-title" style="left:98px;top:741px">Right Hand “Key to Chipping”</h3>
  <div class="abs like" style="left:575px;top:748px"><i></i>Like</div>
  <p class="abs post-meta" style="left:95px;top:766px">Submitted by Larkmoor Golf Club on June 29th, 2011</p>
  <div class="abs thumb" style="left:105px;top:787px"><div role="img" aria-label="Photo: golfers and a cart on the course"></div></div>
  <p class="abs post-body" style="left:209px;top:791px">Lorem Ipsum is simply dummy text of the printing and typesetting industry. Lorem Ipsum has been the industry's standard dummy text ever since the 1500s, when an unknown printer took a galley of type and scrambled it to make a type specimen book. It has survived not only five centuries, but also the leap into electronic typesetting...</p>
  <div class="abs more" style="left:566px;top:861px">Read more...</div>
</article>
<div class="abs rule" style="top:884px"></div>

<article>
  <h3 class="abs post-title" style="left:95px;top:900px">Hinge and Turn on Your Pitch Shot</h3>
  <div class="abs like" style="left:575px;top:904px"><i></i>Like</div>
  <p class="abs post-meta" style="left:95px;top:925px">Submitted by Larkmoor Golf Club on June 30th, 2011</p>
  <div class="abs thumb" style="left:105px;top:946px"><div role="img" aria-label="Promotional golf graphic"></div></div>
  <p class="abs post-body" style="left:209px;top:947px;width:416px">Lorem Ipsum is simply dummy text of the printing and typesetting industry. Lorem Ipsum has been the industry's standard dummy text ever since the 1500s, when an unknown printer took a galley of type and scrambled it to make a type specimen book. It has survived not only five centuries, but also the leap into electronic typesetting...</p>
  <div class="abs more" style="left:566px;top:1022px">Read more...</div>
</article>

<nav aria-label="Pagination">
  <div class="abs pager dark" style="left:207px">Previous</div>
  <div class="abs pager num" style="left:264px">1</div>
  <div class="abs pager num" style="left:289px">2</div>
  <div class="abs pager num" style="left:314px">3</div>
  <div class="abs pager num" style="left:339px">4</div>
  <div class="abs pager num" style="left:364px">5</div>
  <div class="abs pager num" style="left:389px">6</div>
  <div class="abs pager" style="left:409px;width:16px;color:#333">......</div>
  <div class="abs pager dark" style="left:431px">Next</div>
</nav>

<aside class="abs newsletter">
  <svg style="position:absolute;left:11px;top:6px" width="32" height="30" viewBox="0 0 32 30">
    <rect x="2" y="8" width="28" height="20" fill="#f3c23a" stroke="#c48a12"/>
    <path d="M2 8 L16 19 L30 8" fill="none" stroke="#c48a12"/>
    <rect x="8" y="2" width="16" height="12" fill="#fff" stroke="#9ab"/>
  </svg>
  <h3>Subscribe <span>Newsletter</span></h3>
  <p>Lorem Ipsum is simply dummy text of the printing and type setting industry.</p>
  <label style="left:30px;top:88px">Email</label>
  <div class="field" style="top:84px"></div>
  <label style="left:11px;top:114px">Password</label>
  <div class="field" style="top:110px"></div>
  <div class="subscribe">Subscribe ▸</div>
</aside>

<aside class="abs tabs">
  <div class="head"><div class="on">POPULAR</div><div>COMMENTS</div><div>TAGS</div></div>
  <div class="body">
    <div class="item"><p>Phasellus molestie dapibus quam, non tempor dui venenatis eget.</p><div class="row"><span>Marten Cobley</span><span>Dated 02/07/12</span></div></div>
    <div class="item"><p>Phasellus molestie dapibus quam, non tempor dui venenatis eget.</p><div class="row"><span>Marten Cobley</span><span>Dated 02/07/12</span></div></div>
    <div class="item"><p>Phasellus molestie dapibus quam, non tempor dui venenatis eget.</p><div class="row"><span>Marten Cobley</span><span>Dated 02/07/12</span></div></div>
    <div class="item"><p>Phasellus molestie dapibus quam, non tempor dui venenatis eget.</p><div class="row"><span>Marten Cobley</span><span>Dated 02/07/12</span></div></div>
  </div>
</aside>

<div class="abs social" style="top:998px"><span class="sq" style="background:var(--friendspace)"></span><div><div class="t1">Find us on</div><div class="t2">Friendspace</div></div></div>
<div class="abs" style="left:680px;top:1035px;width:174px;border-top:1px dotted #999"></div>
<div class="abs social" style="top:1046px"><span class="sq" style="background:var(--chirpline)"></span><div><div class="t1">follow us on</div><div class="t2">Chirpline</div></div></div>

<footer class="abs footer">
  <div class="brand">LARKMOOR<small>Golf Club</small></div>
  <nav>Home &nbsp; | &nbsp; About &nbsp; | &nbsp; Video Instruction &nbsp; | &nbsp; Instruction &nbsp; | &nbsp; Golf Blog</nav>
  <div class="copy">Copyright © 2012 - larkmoorgolfclub - All rights reserved. Terms and Privacy Policy</div>
  <address><b>Address Line 1 with City</b><br><b>Address Line 2 with Country</b><br>Tel. : 123 . 456 . 7890<br>Email : info@larkmoorgolfclub.example</address>
</footer>
</body>
</html>
```